Its a flyer to a course entitled :
Ultrasound Course

Basically we teach students about the use of ultrasound for very sick patients

-I need a title in 3D
-I need an attractive design please
something extraordinary

Please if you have any ongoing project let me know Thanks

Dear Designers Was looking for something new that I did not see before, unfortunately did not find that yet! To clarify the idea, remember the T.V series 'TQ'.. so we have a sick patient like the one you have seen in the series and now we are using Ultrasound to help get the diagnosis and even it helps us in the procedures so basically will use the ultrasound to help saving those patients and give them the treatment in a short time.j

```html
<!DOCTYPE html>
<html lang="en">
<head>
<meta charset="UTF-8">
<title>Emergency &amp; Critical Care – Ultrasound Course</title>
<link rel="stylesheet" href="https://fonts.googleapis.com/css2?family=Caladea:wght@700&family=Didact+Gothic&display=swap">
<style>
  :root {
    --teal: #2eb2a4;
    --teal-deep: #28a396;
    --navy: #3d5d92;
    --coral: #f1606b;
    --title-red: #d8283f;
    --title-edge: #f3c9cf;
    --pill-top: #6f9ee0;
    --pill-bottom: #263f70;
    --white: #ffffff;
    --rule: #2a2f3a;
  }
  * { margin: 0; padding: 0; box-sizing: border-box; }
  html, body { width: 1200px; height: 2799px; overflow: hidden; background: var(--teal); }
  .flyer {
    position: relative;
    width: 1200px;
    height: 2799px;
    overflow: hidden;
    background: radial-gradient(ellipse at 60% 35%, var(--teal) 0%, var(--teal-deep) 100%);
  }
  .flyer__shapes { position: absolute; inset: 0; width: 1200px; height: 2799px; }
  .title {
    position: absolute;
    left: 0; right: 0;
    top: 300px;
    text-align: center;
    font-family: "Caladea", "Cambria", serif;
    font-weight: 700;
    font-size: 192px;
    line-height: 265px;
    color: var(--title-red);
    text-shadow:
      2px 2px 0 var(--title-edge),
      4px 4px 0 var(--title-edge),
      6px 6px 0 #e7aab3,
      8px 8px 0 #d98e99,
      10px 10px 0 #c77783,
      14px 16px 14px rgba(40, 20, 40, 0.45);
  }
  .title__reflection {
    position: absolute;
    left: 0; right: 0;
    top: 800px;
    text-align: center;
    font-family: "Caladea", "Cambria", serif;
    font-weight: 700;
    font-size: 192px;
    line-height: 200px;
    color: var(--title-red);
    transform: scaleY(-0.55);
    transform-origin: top;
    opacity: 0.18;
  }
  .course-badge {
    position: absolute;
    left: 30px;
    top: 1056px;
    width: 1134px;
    height: 264px;
    border-radius: 132px;
    border: 6px solid #9fb8dc;
    background: linear-gradient(180deg, var(--pill-top) 0%, #3f67a8 45%, var(--pill-bottom) 100%);
    box-shadow: 0 10px 24px rgba(0, 0, 0, 0.35), inset 0 6px 10px rgba(255, 255, 255, 0.35);
    display: flex;
    align-items: center;
    justify-content: center;
    text-align: center;
    font-family: "Caladea", "Cambria", serif;
    font-weight: 700;
    font-size: 100px;
    line-height: 104px;
    color: #eef1f6;
    text-shadow:
      2px 2px 0 #9aa3b2,
      4px 4px 0 #7c8596,
      6px 7px 8px rgba(0, 0, 0, 0.55);
  }
  .intro {
    position: absolute;
    left: 0; right: 0;
    top: 1425px;
    text-align: center;
    font-family: "Didact Gothic", "Century Gothic", sans-serif;
    font-size: 86px;
    line-height: 104px;
    color: var(--white);
  }
  .intro span { display: block; }
  .intro .l1 { padding-left: 60px; }
  .intro .l2 { padding-left: 20px; }
  .intro .l3 { padding-left: 10px; }
  .footer-rule {
    position: absolute;
    left: 225px;
    top: 2592px;
    width: 690px;
    height: 8px;
    border-radius: 4px;
    background: linear-gradient(90deg, rgba(42,47,58,0) 0%, var(--rule) 15%, var(--rule) 85%, rgba(42,47,58,0) 100%);
  }
  .tagline {
    position: absolute;
    left: 0; right: 0;
    top: 2660px;
    text-align: center;
    font-family: "Didact Gothic", "Century Gothic", sans-serif;
    font-size: 80px;
    line-height: 100px;
    color: var(--white);
    padding-left: 20px;
  }
</style>
</head>
<body>
<main class="flyer">
  <svg class="flyer__shapes" viewBox="0 0 1200 2799" aria-hidden="true">
    <polygon class="shape-navy-top" points="0,0 555,0 750,198 180,960 0,735" fill="var(--navy)"/>
    <polygon class="shape-coral-bottom" points="0,2370 810,1965 1200,2200 1200,2799 0,2799" fill="var(--coral)"/>
    <polygon class="shape-navy-right" points="1200,1410 525,2310 1200,2775" fill="var(--navy)"/>
  </svg>

  <h1 class="title">Emergency &amp;<br>Critical Care</h1>
  <div class="title__reflection" aria-hidden="true">Critical Care</div>

  <div class="course-badge">ULTRASOUND<br>COURSE</div>

  <p class="intro">
    <span class="l1">Come here to learn</span>
    <span class="l2">about the use of</span>
    <span class="l3">ULTRASOUND</span>
    <span>for very sick patients</span>
  </p>

  <div class="footer-rule"></div>
  <p class="tagline">PEOPLE NEED YOU !</p>
</main>
</body>
</html>
```